WP website design (TOVI)

We need a wordpress design that will incorporate a professional color scheme with company logo in a clean layout. The design needs to consider that this will be developed on a responsive theme. Colors are undetermined - those that will complement the logo.
Client mentions liking plinmerbid.com for the layout and use of color. Possible but not necessary to have large slideshow element.

Industry/Entity Type

It Company

Font styles to use
Sans Serif

Colors

Designer to choose colors to be used in the design.

Requirements
Must have
• - Navigation: 1)Home 2) Auctions 3) Services 4) About Us 5) FAQs 6) References 7) Contact Us

Site will have slideshow, please use high-end stock real estate image initially. Header will have logo. Social icons (Facebook, Twitter, Youtube)

Widgets Include: Email signup form, Featured Auctions, Featured Video widget.

Footer will have contact info (below), site navigation, smaller company logo, affiliation logos (attached).

TOVI Auction Group
4275 Birch Vale Lane
Marlowe, KY 40617
1-800-419-BIDS (2437)
Ph. (270) 386-9041
Fx. (270) 386-1158
Nice to have
• - Site will have drop-down menus - please indicate the styling, for instance the dropdown menus 1) Live 2) Online 3) Past - under the 'Auctions' link

```html
<!DOCTYPE html>
<html lang="en">
<head>
<meta charset="utf-8">
<title>TOVI Auction Group</title>
<link href="https://fonts.googleapis.com/css2?family=Oswald:wght@300;400&family=Arimo:wght@400;700&display=swap" rel="stylesheet">
<style>
:root{
  --brown:#7f4a14;
  --brown-text:#7a4a12;
  --red:#e0121b;
  --panel:#e9e9e9;
  --ink:#222;
  --footer:#ececec;
  --sky:#b9cde0;
}
*{box-sizing:border-box;margin:0;padding:0}
html,body{width:987px;height:1200px;overflow:hidden;background:#fff}
body{position:relative;font-family:Arimo,Arial,sans-serif;color:var(--ink)}
.abs{position:absolute}
.head-font{font-family:Oswald,"Arial Narrow",sans-serif;font-weight:300}

.header-backdrop{left:0;top:0;width:987px;height:356px;background:linear-gradient(180deg,#d9e2ea 0%,#e6e6e3 45%,#c9cfc3 100%)}
.brand{left:93px;top:24px;width:160px;height:105px;display:flex;align-items:center;gap:8px}
.brand-dot{width:16px;height:16px;border-radius:50%;background:var(--red);flex:none}
.brand-name{font-family:Oswald,sans-serif;font-weight:400;font-size:25px;line-height:1.05;color:var(--red)}

.nav a{position:absolute;top:65px;height:32px;line-height:32px;font-family:Oswald,sans-serif;font-weight:300;font-size:17px;color:#1d1d1d;text-decoration:none}
.nav a.active{color:var(--brown-text);border:1px solid var(--brown);border-radius:3px;width:72px;text-align:center;background:rgba(255,255,255,.35)}

.social span{position:absolute;top:19px;width:34px;height:34px;border-radius:50%;background:var(--brown);border:2px solid #b3874c}

.hero{left:63px;top:134px;width:861px;height:222px;background:linear-gradient(180deg,#8fb3d6 0%,#d9d5cf 40%,#c8bdb2 70%,#5e6c3e 100%)}
.hero-arrow{top:226px;width:30px;height:33px;background:#fff;display:flex;align-items:center;justify-content:center}

.widget{top:386px;height:186px;background:var(--panel);border-radius:5px}
.tab{top:374px;height:30px;background:var(--brown);color:#fff;font-size:19px;display:flex;align-items:center;justify-content:center;gap:8px;text-transform:uppercase}
.tab svg{width:18px;height:18px}

.signup-title{left:63px;top:412px;width:275px;text-align:center;color:var(--brown-text);font-size:12px}
.field{left:85px;width:231px;height:25px;background:#fff;border:1px solid #cfcfcf;font-size:10.5px;padding-left:7px;line-height:23px}
.btn-red{background:var(--red);color:#fff;font-family:Oswald,sans-serif;font-weight:400;text-align:center}
.btn-brown{background:var(--brown);color:#fff;font-family:Oswald,sans-serif;font-weight:400;text-align:center;font-size:16px;line-height:26px}

.lot-thumb{left:369px;width:77px;height:51px;background:linear-gradient(180deg,#7fb0e0,#c9c2b3 55%,#6e9548)}
.lot-text{left:456px;width:160px;font-size:10.5px;line-height:13px}
.lot-links{left:458px;font-size:11px;font-weight:700;color:var(--brown-text)}
.lot-links a{color:inherit;margin-right:26px}
.dotted{left:369px;width:240px;border-top:1px dotted #b5b5b5}

.video{left:656px;top:420px;width:257px;height:137px;background:linear-gradient(180deg,#9cc3e6 0%,#cfc7b3 45%,#6f9a4a 100%)}

.section{left:63px;width:857px;height:186px;background:var(--panel);border-radius:5px}
.section-bar{left:87px;width:811px;height:30px;background:var(--brown);color:#fff;font-size:19px;line-height:30px;padding-left:10px;text-transform:uppercase}
.section-photo{background:linear-gradient(180deg,#6fa6df 0%,#e0dcd2 50%,#6d9446 100%);border:1px solid #bdbdbd}
.section-copy{left:281px;width:340px;font-size:11px;line-height:19px}
.bid-btn{left:685px;width:162px;height:26px;font-size:16px;line-height:26px}
.bid-meta{left:688px;font-size:11px;line-height:19px}
.bid-meta .only{color:var(--brown-text);font-weight:700}
.bid-meta b{font-weight:700}

.footer{left:63px;top:1029px;width:861px;height:171px;background:var(--footer);border-top:4px solid #333}
.foot-nav{left:80px;top:1044px;list-style:none}
.foot-nav li{height:21.4px;line-height:21.4px;font-family:Oswald,sans-serif;font-weight:300;font-size:15px;display:flex;align-items:center;gap:12px}
.foot-nav li::before{content:"";border-left:5px solid #444;border-top:4px solid transparent;border-bottom:4px solid transparent}
.foot-nav li.active{color:var(--red)}
.foot-nav li.active::before{border-left-color:var(--red)}
.foot-contact{left:296px;top:1045px;font-size:11px}
.foot-contact h3{font-family:Oswald,sans-serif;font-weight:400;font-size:17px;color:var(--red);margin-bottom:4px}
.foot-contact p{height:24px;line-height:24px}
.foot-brand{left:521px;top:1061px;width:156px;height:104px;display:flex;align-items:center;gap:8px}
.badge{top:1075px;height:39px;background:#9a9a9a;border-radius:4px}
.copyright{left:722px;top:1149px;font-size:10.5px;line-height:19px;color:#333}
.copyright strong{color:var(--red)}
</style>
</head>
<body>

<div class="abs header-backdrop" role="img" aria-label="Soft, faded photo of a large suburban house behind the header"></div>

<div class="abs brand">
  <span class="brand-dot"></span>
  <span class="brand-name">TOVI Auction Group</span>
</div>

<nav class="nav">
  <a class="active" style="left:356px">Home</a>
  <a style="left:447px">Auctions</a>
  <a style="left:533px">Services</a>
  <a style="left:619px">About</a>
  <a style="left:691px">FAQs</a>
  <a style="left:758px">References</a>
  <a style="left:861px">Contact</a>
</nav>

<div class="social" aria-label="Social links">
  <span style="left:770px"></span>
  <span style="left:818px"></span>
  <span style="left:866px"></span>
</div>

<div class="abs hero" role="img" aria-label="Slideshow photo of a two-storey stucco house with balcony and garden"></div>
<div class="abs hero-arrow" style="left:63px"><svg width="12" height="20" viewBox="0 0 12 20"><path d="M10 1 2 10l8 9" fill="none" stroke="#555" stroke-width="1.6"/></svg></div>
<div class="abs hero-arrow" style="left:894px"><svg width="12" height="20" viewBox="0 0 12 20"><path d="M2 1l8 9-8 9" fill="none" stroke="#555" stroke-width="1.6"/></svg></div>

<!-- Widgets -->
<div class="abs widget" style="left:63px;width:275px"></div>
<div class="abs widget" style="left:355px;width:274px"></div>
<div class="abs widget" style="left:647px;width:274px"></div>

<div class="abs tab head-font" style="left:87px;width:216px">
  <svg viewBox="0 0 20 16"><rect x="1" y="1" width="18" height="14" fill="none" stroke="#fff" stroke-width="1.5"/><rect x="4" y="4" width="5" height="4" fill="#fff"/><path d="M11 5h5M11 8h5M4 11h12" stroke="#fff" stroke-width="1.3"/></svg>
  Newsletter
</div>
<div class="abs tab head-font" style="left:378px;width:217px">
  <svg viewBox="0 0 20 20"><circle cx="10" cy="10" r="6" fill="none" stroke="#fff" stroke-width="4" stroke-dasharray="3 2"/><circle cx="10" cy="10" r="2.5" fill="#fff"/></svg>
  Featured Auction
</div>
<div class="abs tab head-font" style="left:670px;width:217px">
  <svg viewBox="0 0 16 20"><path d="M1 1h9l5 5v13H1z" fill="none" stroke="#fff" stroke-width="1.5"/><path d="M6 9v6l5-3z" fill="#fff"/></svg>
  Featured Video
</div>

<p class="abs signup-title">Create your Account</p>
<div class="abs field" style="top:433px">Email</div>
<div class="abs field" style="top:467px">Username</div>
<div class="abs field" style="top:501px">Password</div>
<div class="abs btn-red" style="left:149px;top:536px;width:94px;height:25px;font-size:17px;line-height:25px">Create</div>

<div class="abs lot-thumb" style="top:417px" role="img" aria-label="Thumbnail of a suburban house"></div>
<p class="abs lot-text" style="top:421px">Lorem Ipsum is simply dummy text Lorem Ipsum is simply...</p>
<p class="abs lot-links" style="top:453px"><a>Details</a><a>Photos</a></p>
<div class="abs dotted" style="top:478px"></div>
<div class="abs lot-thumb" style="top:486px" role="img" aria-label="Thumbnail of a white house with trees"></div>
<p class="abs lot-text" style="top:490px">Lorem Ipsum is simply dummy text Lorem Ipsum is simply...</p>
<p class="abs lot-links" style="top:522px"><a>Details</a><a>Photos</a></p>
<div class="abs dotted" style="top:552px"></div>

<div class="abs video" role="img" aria-label="Video still of a bungalow with flower beds and lawn"></div>
<svg class="abs" style="left:763px;top:453px" width="42" height="42" viewBox="0 0 42 42"><circle cx="21" cy="21" r="19" fill="rgba(255,255,255,.25)" stroke="rgba(255,255,255,.7)" stroke-width="3"/><path d="M16 12v18l14-9z" fill="rgba(255,255,255,.75)"/></svg>

<!-- Online personal property auction -->
<div class="abs section" style="top:601px"></div>
<div class="abs section-bar head-font" style="top:589px">Online Personal Property Auction</div>
<div class="abs section-photo" style="left:90px;top:637px;width:176px;height:95px" role="img" aria-label="Photo of a two-storey home with landscaped front yard"></div>
<div class="abs btn-brown" style="left:136px;top:743px;width:94px;height:26px">Details</div>
<p class="abs section-copy" style="top:631px">Lorem Ipsum is simply dummy text of the printing and typesetting industry. Lorem Ipsum has been the industry's standard dummy text ever since the 1500s, when an unknown printer took a galley of type and scrambled it to make a type specimen book. It has survived not only five centuries, but also the leap into electronic</p>
<div class="abs btn-red bid-btn" style="top:636px">Click for Online Bidding</div>
<div class="abs bid-meta" style="top:666px">
  <div class="only">Online Bidding Only</div>
  <div><b>Began:</b>&nbsp; 10/03/14 at 9:00 AM&nbsp; EDT</div>
  <div><b>Ends:</b>&nbsp; 10/09/14 at 7:00 PM&nbsp; EDT</div>
</div>

<!-- Online real estate auction -->
<div class="abs section" style="top:817px"></div>
<div class="abs section-bar head-font" style="top:805px">Online Real Estate Auction</div>
<div class="abs section-photo" style="left:87px;top:850px;width:176px;height:95px" role="img" aria-label="Photo of a farmhouse on a green lawn"></div>
<div class="abs btn-brown" style="left:136px;top:960px;width:94px;height:26px">Details</div>
<p class="abs section-copy" style="top:848px">Lorem Ipsum is simply dummy text of the printing and typesetting industry. Lorem Ipsum has been the industry's standard dummy text ever since the 1500s, when an unknown printer took a galley of type and scrambled it to make a type specimen book. It has survived not only five centuries, but also the leap into electronic</p>
<div class="abs btn-red bid-btn" style="top:853px">Click for Online Bidding</div>
<div class="abs bid-meta" style="top:883px">
  <div class="only">Online Bidding Only</div>
  <div><b>Began:</b>&nbsp; 10/03/14 at 9:00 AM&nbsp; EDT</div>
  <div><b>Ends:</b>&nbsp; 10/09/14 at 7:00 PM&nbsp; EDT</div>
</div>

<!-- Footer -->
<div class="abs footer"></div>
<ul class="abs foot-nav">
  <li class="active">Home</li>
  <li>Auctions</li>
  <li>Services</li>
  <li>About</li>
  <li>FAQs</li>
  <li>References</li>
  <li>Contact</li>
</ul>
<div class="abs foot-contact">
  <h3>TOVI Auction Group</h3>
  <p>4275 Birch Vale Lane</p>
  <p>Marlowe, KY 40617</p>
  <p>1-800-419-BIDS (2437)</p>
  <p>Call:&nbsp; (270) 386-9041</p>
  <p>FAX :&nbsp; (270) 386-1158</p>
</div>
<div class="abs foot-brand">
  <span class="brand-dot"></span>
  <span class="brand-name">TOVI Auction Group</span>
</div>
<div class="abs badge" style="left:724px;width:30px"></div>
<div class="abs badge" style="left:763px;width:62px;border-radius:50%"></div>
<div class="abs badge" style="left:831px;width:38px"></div>
<div class="abs badge" style="left:880px;width:33px"></div>
<div class="abs copyright">
  <div>Copyright © 2014 • <strong>TOVI Auction Group</strong></div>
  <div>• All Rights Reserved</div>
</div>

</body>
</html>
```